Velanqua Cookbook (Independant Velanqua Consultant - not Velanqua themselves)

Approx 120 page Recipe book, need design created for recipe pages.
each recipe illustrated with full colour photograph (supplied) on opposite page.
To included index, contents page, intro, etc
Cover design also to be suggested.
We must have a professional finish, but with a friendly, family theme.
Reason: Deadline extended because I require further designs, please.

```html
<!DOCTYPE html>
<html lang="en">
<head>
<meta charset="utf-8">
<title>Red Capsicum and Broccoli Salad – Velanqua Cookbook</title>
<link rel="stylesheet" href="https://fonts.googleapis.com/css2?family=Open+Sans:wght@400;600;700&family=Carlito:wght@400;700&display=swap">
<style>
  :root {
    --page-bg: #f1f2f3;
    --page-bg-edge: #e6e8ea;
    --photo-red: #c8452e;
    --photo-green: #8a9a4a;
    --photo-cream: #e9e2cf;
    --photo-sky: #dfe3e6;
    --title-band: #e4e6e5;
    --title-green: #1f5d3a;
    --accent-green: #2f8f3a;
    --card-green-top: #7cc24a;
    --card-green-mid: #99d066;
    --card-green-bottom: #bfe08a;
    --heading-green: #1d4f2e;
    --body-text: #ffffff;
    --leaf-light: rgba(150, 205, 95, 0.85);
    --leaf-dark: rgba(92, 160, 55, 0.85);
  }
  * { box-sizing: border-box; margin: 0; padding: 0; }
  html, body { width: 1200px; height: 682px; overflow: hidden; background: var(--page-bg); }
  .spread { position: relative; width: 1200px; height: 682px; overflow: hidden; }

  .photo-page {
    position: absolute; left: 0; top: 0; width: 600px; height: 682px;
    background: linear-gradient(170deg, var(--photo-sky) 0%, #c9cfc9 14%, var(--photo-green) 26%, #b4593a 48%, var(--photo-red) 62%, #9a7a42 82%, var(--photo-cream) 100%);
  }

  .recipe-page {
    position: absolute; left: 600px; top: 0; width: 600px; height: 682px;
    background: linear-gradient(90deg, var(--page-bg) 0%, #f6f7f8 50%, var(--page-bg-edge) 100%);
  }

  .recipe-card {
    position: absolute; left: 35px; top: 73px; width: 526px; height: 575px;
    background: linear-gradient(180deg, var(--card-green-top) 0%, var(--card-green-mid) 55%, var(--card-green-bottom) 100%);
  }
  .title-band {
    position: absolute; left: 0; top: 0; width: 100%; height: 90px;
    background: var(--title-band);
    text-align: center; padding-top: 6px;
  }
  .recipe-title {
    font-family: "Open Sans", sans-serif; font-weight: 700;
    font-size: 22px; line-height: 28px; color: var(--title-green);
    letter-spacing: 0.3px;
  }
  .diet-tags {
    font-family: "Open Sans", sans-serif; font-weight: 700;
    font-size: 13px; line-height: 18px; color: var(--accent-green);
    letter-spacing: 0.5px;
  }

  .column-heading {
    position: absolute; top: 113px;
    font-family: "Carlito", "Open Sans", sans-serif; font-weight: 400;
    font-size: 24px; color: var(--heading-green); letter-spacing: 0.5px;
  }
  .column-heading.ingredients-heading { left: 14px; }
  .column-heading.method-heading { left: 191px; }

  .ingredient-list, .method-list {
    position: absolute; list-style: none;
    font-family: "Carlito", "Open Sans", sans-serif; font-weight: 700;
    font-size: 11.5px; color: var(--body-text);
  }
  .ingredient-list { left: 14px; top: 156px; width: 160px; }
  .ingredient-list li { position: absolute; left: 0; white-space: nowrap; }

  .method-list { left: 175px; top: 156px; width: 302px; }
  .method-list li { position: absolute; left: 0; right: 0; padding-left: 16px; line-height: 14px; }
  .method-list li::before {
    content: ""; position: absolute; left: 3px; top: 5px;
    width: 4px; height: 4px; border-radius: 50%; background: var(--body-text);
  }

  .dish-thumbnail {
    position: absolute; left: 425px; top: 18px; width: 180px; height: 180px;
    border-radius: 50%; border: 5px solid #ffffff;
    background: linear-gradient(160deg, var(--photo-green) 0%, #b96a3c 45%, var(--photo-red) 70%, var(--photo-cream) 100%);
  }

  .leaf-area {
    position: absolute; left: 5px; top: 457px; width: 225px; height: 225px;
    background: linear-gradient(135deg, var(--leaf-light) 0%, var(--leaf-dark) 100%);
  }
</style>
</head>
<body>
<main class="spread">
  <section class="photo-page" role="img" aria-label="Photograph of red capsicum and broccoli salad on a white serving dish with fresh capsicums and broccoli behind"></section>

  <section class="recipe-page">
    <article class="recipe-card">
      <header class="title-band">
        <h1 class="recipe-title">RED CAPSICUM AND<br>BROCCOLI SALAD</h1>
        <p class="diet-tags">GF DF EF</p>
      </header>

      <h2 class="column-heading ingredients-heading">INGREDIENT</h2>
      <h2 class="column-heading method-heading">RECIPE</h2>

      <ul class="ingredient-list">
        <li style="top:0">3 rashers bacon</li>
        <li style="top:32px">1 red pepper</li>
        <li style="top:61px">¼ small red onion</li>
        <li style="top:87px">1 head broccoli</li>
        <li style="top:116px">45g cranberries or sultanas</li>
        <li style="top:146px">30g slivered almonds</li>
        <li style="top:175px">French Dressing</li>
      </ul>

      <ul class="method-list">
        <li style="top:0">Chop bacon into large pieces. Pan fry until crisp. Place into VQ bowl.</li>
        <li style="top:42px">Cut red pepper and onion into pieces and add to bowl.</li>
        <li style="top:73px">Chop for 3 seconds on Speed 4.</li>
        <li style="top:101px">Cut broccoli into florets.&nbsp; Add to bowl with cranberries and almonds.</li>
        <li style="top:147px">Chop 5 seconds, Speed 4 or until chopped to desired size.</li>
        <li style="top:175px">Place in serving bowl and drizzle with dressing.</li>
      </ul>
    </article>

    <div class="dish-thumbnail" role="img" aria-label="Round close-up photograph of the salad garnished with parsley"></div>
    <div class="leaf-area" role="img" aria-label="Illustration of fresh green leaves"></div>
  </section>
</main>
</body>
</html>
```